Dancing Otter Coffee Co menu

We would like our existing menu tidied up.
we want to keep the all the items, but need it less busy and clearer to read.

Also want to leave a bit of space to add a few item in the future.

```html
<!DOCTYPE html>
<html lang="en">
<head>
<meta charset="utf-8">
<title>Dancing Otter Coffee Co – Menu</title>
<link rel="stylesheet" href="https://fonts.googleapis.com/css2?family=Cinzel:wght@500;600&family=EB+Garamond:ital,wght@0,400;0,500;1,400&family=Rye&display=swap">
<style>
  :root {
    --backdrop: #4a4a4a;
    --paper: #ffffff;
    --brown: #4e2607;
    --ink: #1f1f1f;
    --bar-text: #ffffff;
  }
  * { box-sizing: border-box; margin: 0; padding: 0; }
  html, body {
    width: 1200px; height: 1052px; overflow: hidden;
    background: var(--backdrop);
  }
  .menu-page {
    position: absolute; left: 228px; top: 0;
    width: 744px; height: 1052px;
    background: var(--paper);
    color: var(--ink);
    font-family: "EB Garamond", Georgia, serif;
  }
  .page-frame { position: absolute; inset: 0; }

  .brand {
    position: absolute; left: 66px; top: 56px;
    display: flex; align-items: center; gap: 12px;
  }
  .brand-mark {
    width: 34px; height: 34px; border-radius: 50%;
    background: var(--ink); flex: none;
  }
  .brand-name {
    font-family: "Cinzel", Georgia, serif; font-weight: 600;
    font-size: 26px; line-height: 1.1; color: var(--ink);
    letter-spacing: 1px; width: 230px;
  }

  .title-block {
    position: absolute; left: 420px; top: 74px; width: 250px;
    text-align: center; color: var(--ink);
    font-family: "Rye", Georgia, serif;
  }
  .title-main { font-size: 56px; line-height: 1; }
  .title-sub { font-size: 24px; line-height: 1; margin-top: 2px; }

  .column { position: absolute; }
  .column-left { left: 66px; top: 172px; width: 286px; }
  .column-right { left: 408px; top: 230px; width: 272px; }

  .section-heading {
    display: flex; align-items: center; gap: 10px;
    font-family: "EB Garamond", Georgia, serif; font-weight: 500;
    font-size: 16px; letter-spacing: 1.5px; text-transform: uppercase;
    margin-bottom: 6px;
  }
  .section-heading::after {
    content: ""; flex: 1; height: 2px; background: var(--brown);
  }
  .section-heading.plain { text-transform: none; letter-spacing: 0.3px; font-size: 16px; }

  .item { margin-bottom: 14px; }
  .item-bar {
    display: flex; justify-content: space-between; align-items: center;
    background: var(--brown); color: var(--bar-text);
    height: 18px; padding: 0 8px;
    font-family: "Cinzel", Georgia, serif; font-weight: 500;
    font-size: 11.5px; letter-spacing: 1.2px;
  }
  .item-price { font-family: "EB Garamond", Georgia, serif; font-size: 12px; letter-spacing: 0.5px; }
  .item-desc { font-style: italic; font-size: 11.5px; line-height: 1.2; margin-top: 2px; width: 210px; }
  .item-desc b { font-style: normal; font-weight: 500; font-size: 12.5px; }
  .item-sizes { font-size: 12.5px; font-weight: 500; margin-top: 2px; letter-spacing: 0.3px; }

  .extras { display: flex; justify-content: space-between; align-items: flex-start;
    font-size: 12px; font-weight: 500; line-height: 1.15; margin: 6px 0 22px; }
  .extras-list { width: 200px; text-transform: uppercase; }

  .ribbon {
    margin: 22px 0 10px -4px; width: 266px; height: 30px;
    position: relative; color: var(--bar-text);
    font-family: "EB Garamond", Georgia, serif; font-weight: 500;
    font-size: 18px; letter-spacing: 1px; text-transform: uppercase;
  }
  .ribbon svg { position: absolute; inset: 0; }
  .ribbon span { position: relative; display: block; text-align: center; line-height: 30px; }

  .special { margin-bottom: 16px; }
  .special .item-bar { width: 280px; height: 18px; }
  .special .item-bar.double { height: 34px; align-items: center; line-height: 1.1; }
  .special-text { font-size: 12.5px; line-height: 1.2; margin-top: 6px; width: 250px; }
</style>
</head>
<body>
<main class="menu-page">
  <svg class="page-frame" width="744" height="1052" viewBox="0 0 744 1052">
    <g fill="none" stroke="var(--brown)" stroke-width="3">
      <polyline points="52,62 44,62 44,990 694,990 694,52 420,52"/>
    </g>
  </svg>

  <div class="brand">
    <span class="brand-mark"></span>
    <span class="brand-name">Dancing Otter Coffee Co</span>
  </div>

  <div class="title-block">
    <div class="title-main">Coffee</div>
    <div class="title-sub">&amp; Tea</div>
  </div>

  <section class="column column-left">
    <h2 class="section-heading">Coffee</h2>

    <div class="item">
      <div class="item-bar"><span>Flat White</span><span class="item-price">$ 5.00</span></div>
      <p class="item-desc">Espresso shot with a steamed milk.</p>
      <p class="item-sizes">Small $5 - Medium $6 - Large $7</p>
    </div>
    <div class="item">
      <div class="item-bar"><span>Cappuccino</span><span class="item-price">$ 5.00</span></div>
      <p class="item-desc">Espresso shot with a steamed milk, a thick layer of milk foam &amp; chocolate powder topping.</p>
      <p class="item-sizes">Small $5 - Medium $6 - Large $7</p>
    </div>
    <div class="item">
      <div class="item-bar"><span>Latte</span><span class="item-price">$ 5.00</span></div>
      <p class="item-desc">Espresso shot with a steamed milk &amp; a thin layer of milk foam.</p>
      <p class="item-sizes">Small $5 - Medium $6 - Large $7</p>
    </div>
    <div class="item">
      <div class="item-bar"><span>Americano</span><span class="item-price">$ 5.00</span></div>
      <p class="item-desc"><b>Americano</b> - Espresso shot topped up with hot water.<br><b>Long Black</b> - Hot water topped off with espresso shot.</p>
      <p class="item-sizes">Small $5 - Medium $6 - Large $7</p>
    </div>
    <div class="item">
      <div class="item-bar"><span>Espresso</span><span class="item-price">$ 3.00</span></div>
      <p class="item-desc">Double espresso shot.</p>
    </div>
    <div class="item">
      <div class="item-bar"><span>Filter/Batch Brew Coffee</span><span class="item-price">$ 4.00</span></div>
      <p class="item-sizes">Small $4 - Medium $4 - Large $4</p>
    </div>

    <div class="ribbon">
      <svg width="266" height="30" viewBox="0 0 266 30"><polygon points="0,0 266,0 254,15 266,30 0,30 12,15" fill="var(--brown)"/></svg>
      <span>Specialty Drinks</span>
    </div>

    <div class="special">
      <div class="item-bar"><span>Honey Brewed Chai</span><span class="item-price">$ 7.00</span></div>
      <p class="special-text">Our Honey Chai is handmade and blended in Western Australia. It is made from the finest black tea leaves available, aromatic freshly ground spices and infused with locally sourced raw honey. Serve with a choice of steamed milk.</p>
    </div>
    <div class="special">
      <div class="item-bar double"><span>Colombian Cacoa Salted<br>Caramel Hot Chocolate</span><span class="item-price">$ 7.00</span></div>
      <p class="special-text">Made with deep toned and rich cocoa sourced from ancient cocao growing regions of Colombia and sweetened with just enough organic unrefined Colombian panela, all balanced perfectly with a caramel PURE natural infusion and pink Himalayan rock salt. Served with a choice of steamed milk</p>
    </div>
  </section>

  <section class="column column-right">
    <h2 class="section-heading">Tea &amp; Other Drinks</h2>

    <div class="item">
      <div class="item-bar"><span>Organic Green Tea</span><span class="item-price">$ 5.00</span></div>
      <p class="item-sizes">Small $5 - Medium $6 - Large $7</p>
    </div>
    <div class="item">
      <div class="item-bar"><span>English Breakfast Tea</span><span class="item-price">$ 5.00</span></div>
      <p class="item-sizes">Small $5 - Medium $6 - Large $7</p>
    </div>
    <div class="item">
      <div class="item-bar"><span>Organic Earl Grey Tea</span><span class="item-price">$ 5.00</span></div>
      <p class="item-sizes">Small $5 - Medium $6 - Large $7</p>
    </div>
    <div class="item">
      <div class="item-bar"><span>Hot Chocolate</span><span class="item-price">$ 5.00</span></div>
      <p class="item-sizes">Small $5 - Medium $6 - Large $7</p>
    </div>
    <div class="item">
      <div class="item-bar"><span>Dark Cocoa Hot Chocolate</span><span class="item-price">$ 5.00</span></div>
      <p class="item-sizes">Small $5 - Medium $6 - Large $7</p>
    </div>
    <div class="item">
      <div class="item-bar"><span>Chai Latte</span><span class="item-price">$ 5.00</span></div>
      <p class="item-sizes">Small $5 - Medium $6 - Large $7</p>
    </div>

    <h2 class="section-heading plain">PURE Natural Infusions</h2>
    <div class="extras">
      <p class="extras-list">Caramel, Vanilla, Chai Spice, Hazelnut, Belgian Chocolate</p>
      <p>$ 0.50</p>
    </div>

    <h2 class="section-heading plain">Milks</h2>
    <div class="extras">
      <p class="extras-list">Full Cream, Skinny, Oat, Almond, Soy.</p>
      <p>$ INC</p>
    </div>
  </section>
</main>
</body>
</html>
```